Stationery and Logo Design Project for new NZ Accounting Firm

Our company name is based in Auckland, New Zealand and is called TMV CA Limited. We are a chartered accountancy firm hence the CA abbreviations.

We need a full logo stationery design: Logo, Letterhead, Business Card and Compliments slip.

We are looking for a bold, modern and clean/simple design that makes us stand out. We want to stand out as professionals in the industry and would like the logo and stationery that our clients see to convey this image. We also want to break away from the traditional boring views of book/bean accountants. We are not doing the same old things others are doing and are mainly cloud based but with face to face business relationship focused as well.

We see ourselves as business advisers that provide more than just filing their tax returns. We want to add value to their business and be a partner in their business ventures.

We want the logo to convey the above and also attract potential clients when they see our ads among the thousands on zarvo and the tallow index.

The logo can be for the "TMV" with CA Ltd seperately or a logo/design beside the TMV. But open to other suggestions or concept.

Hi Designers

The designs I have received so far is not quite what I want.

I want something modern and bold that is DIFFERENT from others, from the usual logo designs. Some logo that when people look at it they will remember it as opposed to fading in the background of other competitors' logo.

Lower case lettering for the TMV could be something to explore as I have not seen a lot of these and they do appeal to me.

Thanks

We can focus on the logo first as that will form the main part for all stationery.

Reason: Final stages of choosing a logo design so need to time for designers to submit the letterhead, namecards designs.

Target Market(s)

Our target clients are small to medium business ranging from the sole trader to 50 employees businesses

Industry/Entity Type

Business

```html
<!DOCTYPE html>
<html lang="en">
<head>
<meta charset="utf-8">
<title>TMV CA Ltd – Business Card</title>
<link rel="stylesheet" href="https://fonts.googleapis.com/css2?family=Ubuntu:wght@400;500;700&display=swap">
<style>
  :root {
    --brand-orange: #f6951f;
    --text-grey: #808184;
    --card-border: #d4d4d4;
    --paper: #ffffff;
  }
  * { margin: 0; padding: 0; box-sizing: border-box; }
  html, body {
    width: 1200px;
    height: 1000px;
    overflow: hidden;
    background: var(--paper);
    font-family: "Ubuntu", Arial, sans-serif;
  }
  .canvas { position: relative; width: 1200px; height: 1000px; }

  .card { position: absolute; top: 350px; width: 533px; height: 301px; }

  /* Front */
  .card-front {
    left: 32px;
    background: var(--paper);
    border: 2px solid var(--card-border);
  }
  .wordmark {
    position: absolute;
    left: 27px;
    top: 125px;
    color: var(--brand-orange);
    font-weight: 700;
    font-size: 38px;
    line-height: 1;
    letter-spacing: -0.5px;
    white-space: nowrap;
  }
  .holder {
    position: absolute;
    right: 32px;
    top: 54px;
    text-align: right;
  }
  .holder-name {
    color: var(--text-grey);
    font-weight: 700;
    font-size: 21px;
    line-height: 26px;
  }
  .holder-title {
    color: var(--brand-orange);
    font-size: 17px;
    line-height: 24px;
  }
  .contact-list {
    position: absolute;
    left: 285px;
    top: 161px;
    list-style: none;
    font-size: 17px;
    line-height: 19.7px;
    color: var(--text-grey);
  }
  .contact-list li { display: flex; white-space: nowrap; }
  .contact-label {
    width: 22px;
    color: var(--brand-orange);
    font-size: 15px;
  }
  .contact-value.small-caps-line { font-size: 16px; }

  /* Back */
  .card-back {
    left: 638px;
    width: 532px;
    height: 300px;
    background: var(--brand-orange);
    color: var(--paper);
  }
  .address {
    position: absolute;
    left: 30px;
    top: 29px;
    font-style: normal;
    font-size: 23px;
    line-height: 29.5px;
  }
  .back-web {
    position: absolute;
    right: 30px;
    top: 228px;
    font-weight: 700;
    font-size: 41px;
    line-height: 1;
    letter-spacing: -0.5px;
  }
</style>
</head>
<body>
<main class="canvas">
  <section class="card card-front" aria-label="Business card front">
    <div class="wordmark">TMV CA Ltd</div>

    <div class="holder">
      <p class="holder-name">Daniel Hart</p>
      <p class="holder-title">BCom, CA</p>
    </div>

    <ul class="contact-list">
      <li><span class="contact-label">E</span><span class="contact-value">daniel@tmv.co.nz</span></li>
      <li><span class="contact-label">M</span><span class="contact-value">021-437051</span></li>
      <li><span class="contact-label">P</span><span class="contact-value small-caps-line">0800 TMVCA LTD (868225)</span></li>
      <li><span class="contact-label">W</span><span class="contact-value">www.tmv.co.nz</span></li>
    </ul>
  </section>

  <section class="card card-back" aria-label="Business card back">
    <address class="address">
      118 Karaka Street<br>
      PO Box 52806<br>
      Harrow Bay<br>
      Auckland 1052
    </address>
    <p class="back-web">www.tmv.co.nz</p>
  </section>
</main>
</body>
</html>
```